依頼詳細
添付の内容を記載したWeb用チラシデザインをお願いします。
記載項目
添付参照
サイズ
A4
ページ数
片面
希望イメージ
シンプル 複雑
単色 カラフル
暗い 明るい
日常 高級
遊び心 厳粛
未来的 伝統的
女性的 男性的
希望する色
納品ファイル
• イラストレーター形式 (.ai)
補足説明
チラシ(例).pdf :こちらの文言を利用したデザインをお願いします。
社名ロゴ:アオバライフ札幌となっていますが、今回のチラシは「アオバライフ東京」と書き換えて使用してください。
エンブレム:使用されてもされなくても構いません。
■ 選んだ理由

大変好感の持てるデザインでした。

■ 提案者全員のお礼・コメント

多数ご提案いただきまして、誠にありがとうございました。
また機会がありましたら、ご提案の程よろしくお願い致します。

```html
<!DOCTYPE html>
<html lang="ja">
<head>
<meta charset="utf-8">
<title>アオバライフ東京 お友達紹介キャンペーン</title>
<link rel="stylesheet" href="https://fonts.googleapis.com/css2?family=M+PLUS+Rounded+1c:wght@500;700;800;900&family=Noto+Sans+JP:wght@400;700;900&display=swap">
<style>
:root{
  --pink:#e4307e;
  --pink-soft:#f07aa8;
  --green:#2f8f3a;
  --green-light:#7fc24a;
  --navy:#1c3f8c;
  --ink:#333;
  --white:#fff;
  --sky:#e9f3f7;
  --gold:#d9b45a;
}
*{margin:0;padding:0;box-sizing:border-box}
html,body{width:859px;height:1200px;overflow:hidden;background:var(--white)}
body{font-family:"M PLUS Rounded 1c","Noto Sans JP",sans-serif;color:var(--ink)}
.flyer{position:relative;width:859px;height:1200px;overflow:hidden;background:var(--white)}
.hero-photo{position:absolute;left:0;top:0;width:859px;height:650px;
  background:linear-gradient(170deg,#dfeef5 0%,#f3ece6 40%,#f7f3ef 70%,#eef6ea 100%)}
.anniv{position:absolute;right:112px;top:18px;color:var(--pink);font-size:14px;font-weight:700;text-align:right;line-height:1.35;white-space:nowrap}
.emblem{position:absolute;right:14px;top:8px;width:86px;height:86px;border-radius:50%;
  background:radial-gradient(circle at 35% 35%,#f6e3a6,var(--gold));border:4px solid #fff;box-shadow:0 2px 4px rgba(0,0,0,.15)}
.headline{position:absolute;left:520px;top:62px;color:var(--pink);font-weight:900;font-size:58px;line-height:1.12;white-space:nowrap;
  text-shadow:0 0 6px #fff,0 0 6px #fff,0 0 6px #fff}
.bubble{position:absolute;left:90px;top:280px;width:130px;height:130px;border-radius:50%;background:var(--pink-soft);
  color:var(--white);font-weight:700;font-size:16px;line-height:1.4;display:flex;align-items:center;justify-content:center;text-align:center}
.limited{position:absolute;left:0;top:420px;width:859px;text-align:center;color:var(--green);font-weight:900;font-size:42px;
  text-shadow:0 0 4px #fff,0 0 4px #fff,0 0 4px #fff}
.points{position:absolute;left:0;top:470px;width:859px;text-align:center;color:var(--pink);font-weight:900;
  text-shadow:3px 0 #fff,-3px 0 #fff,0 3px #fff,0 -3px #fff,2px 2px #fff,-2px -2px #fff,2px -2px #fff,-2px 2px #fff}
.points .num{display:block;font-size:104px;line-height:1;letter-spacing:-2px}
.points .num small{font-size:70px}
.points .get{display:block;font-size:70px;line-height:1.15}
.steps-panel{position:absolute;left:0;top:650px;width:859px;height:450px;background:linear-gradient(180deg,var(--green-light),var(--green))}
.steps-label{position:absolute;left:34px;top:24px;width:130px;height:300px;background:var(--white);border-radius:20px;
  writing-mode:vertical-rl;color:var(--pink);font-weight:800;font-size:26px;line-height:1.45;display:flex;align-items:center;justify-content:center;padding:10px}
.steps{position:absolute;left:184px;top:26px;width:642px;list-style:none}
.step{display:flex;align-items:center;height:62px;margin-bottom:17px;background:var(--white);border-radius:31px;padding-left:8px;box-shadow:0 2px 3px rgba(0,0,0,.15)}
.step-badge{flex:none;width:50px;height:50px;border-radius:50%;background:var(--green);color:var(--white);
  display:flex;flex-direction:column;align-items:center;justify-content:center;font-size:11px;font-weight:700;line-height:1}
.step-badge b{font-size:22px}
.step-text{margin-left:14px;color:var(--navy);font-weight:800;font-size:20px;white-space:nowrap}
.step-text small{font-size:11px;font-weight:500;margin-left:6px}
.notes{position:absolute;left:34px;top:362px;width:792px;display:flex;gap:10px;color:var(--white);font-family:"Noto Sans JP",sans-serif}
.notes-title{flex:none;background:var(--white);color:var(--green);font-size:12px;font-weight:700;padding:3px 8px;border-radius:4px;height:22px}
.notes p{font-size:11px;line-height:1.6}
.footer{position:absolute;left:0;top:1100px;width:859px;height:100px;background:var(--white);display:flex;align-items:center;padding:0 30px}
.brand{display:flex;align-items:center;gap:10px;color:var(--green);font-weight:900;font-size:36px}
.brand-mark{width:26px;height:26px;border-radius:50%;background:var(--green)}
.contact{margin-left:auto;color:var(--navy)}
.tel{display:flex;align-items:center;gap:6px;font-size:40px;font-weight:900;line-height:1}
.tel svg{width:34px;height:34px}
.mail{font-size:14px;font-family:"Noto Sans JP",sans-serif;margin-top:4px}
</style>
</head>
<body>
<main class="flyer">
  <div class="hero-photo" role="img" aria-label="白衣姿の看護師二人の写真"></div>
  <p class="anniv">アオバライフ<br>30周年特別企画！</p>
  <div class="emblem" role="img" aria-label="30周年記念エンブレム"></div>
  <h1 class="headline">お友達に<br>お仕事<br>紹介しま<br>せんか！</h1>
  <p class="bubble">お友達の<br>ナースを<br>ご紹介<br>いただくと</p>
  <p class="limited">サポートナース限定</p>
  <p class="points"><span class="num">30,000<small>point</small></span><span class="get">GETのチャンス！</span></p>

  <section class="steps-panel">
    <p class="steps-label">お友達のナースを紹介してポイントゲットのチャンス！</p>
    <ol class="steps">
      <li class="step"><span class="step-badge">Step<b>1</b></span><span class="step-text">サポートナース経験者の方又は活動中の方が対象</span></li>
      <li class="step"><span class="step-badge">Step<b>2</b></span><span class="step-text">看護師のお友達を紹介して頂きます！<small>※SP対象者</small></span></li>
      <li class="step"><span class="step-badge">Step<b>3</b></span><span class="step-text">お友達がサポートナースとして入職！</span></li>
      <li class="step"><span class="step-badge">Step<b>4</b></span><span class="step-text">入職後３ヶ月経過したら 30,000 ポイントをプレゼント！</span></li>
    </ol>
    <div class="notes">
      <span class="notes-title">注意事項</span>
      <p>お友達が既に登録済みの場合は対象外となります。ポイントは入職から３ヶ月経過後に付与されます。<br>詳しい条件は担当者までお気軽にお問い合わせください。期間は予告なく変更する場合があります。</p>
    </div>
  </section>

  <footer class="footer">
    <div class="brand"><span class="brand-mark"></span>アオバライフ東京</div>
    <div class="contact">
      <div class="tel">
        <svg viewBox="0 0 24 24" aria-hidden="true"><path fill="currentColor" d="M6.6 10.8a15.1 15.1 0 0 0 6.6 6.6l2.2-2.2c.3-.3.7-.4 1-.2 1.1.4 2.3.6 3.6.6.6 0 1 .4 1 1V20c0 .6-.4 1-1 1A17 17 0 0 1 3 4c0-.6.4-1 1-1h3.5c.6 0 1 .4 1 1 0 1.3.2 2.5.6 3.6.1.3 0 .7-.2 1z"/></svg>
        TEL 0120-3941-52
      </div>
      <p class="mail">E-mail / tokyo@aobalife-example.jp</p>
    </div>
  </footer>
</main>
</body>
</html>
```